Brightvale Capital brochure for Investment partnership, young harold pemby

We need a brochure design to attract new investors for our investing partnership Called Brighttvale Capital. We are based in New Orleans, La. We primarily invest in stocks, bonds, and crypto but venture out into other categories as well. We would like to see designs with the black and gold like our logo. The final design should say new, fresh, sleek, tech, and honorable. BROUCHURE WILL BE 4 pages.or one folded sheet a paparer if that makes sense.

A chart showing Brighttvae Capital gains since 2019 28.6 percent and the KT 300 gAINS 7.1 PERCENT

Probable Investors

Financial Planning

• Black and Gold accent. Stock market feel. Sleek, High tech, innovative, Intellgent design.
• Page colors possibly black.
• Boring, Old school,

```html
<!DOCTYPE html>
<html lang="en">
<head>
<meta charset="utf-8">
<title>Brightvale Capital – Brochure</title>
<link rel="stylesheet" href="https://fonts.googleapis.com/css2?family=Cinzel:wght@400;700&family=Tinos:wght@400;700&family=Playfair+Display:wght@700&display=swap">
<style>
  :root {
    --stage: #454545;
    --paper: #f4f4f4;
    --paper-soft: #e9e9e9;
    --ink: #1c1c1c;
    --black: #050505;
    --charcoal: #2f2f2f;
    --gold: #c9a633;
    --gold-light: #ecd46a;
    --gold-deep: #a88a22;
    --cream: #fbf3cf;
    --white: #ffffff;
  }
  * { margin: 0; padding: 0; box-sizing: border-box; }
  html, body { width: 864px; height: 1200px; overflow: hidden; }
  body { background: var(--stage); position: relative; font-family: "Tinos", "Times New Roman", serif; color: var(--ink); }

  .spread { position: absolute; left: 86px; width: 692px; height: 489px; overflow: hidden;
    background: linear-gradient(90deg, var(--paper) 0%, #fafafa 47%, var(--paper-soft) 50%, #fafafa 53%, var(--paper) 100%); }
  .spread--outer { top: 75px; }
  .spread--inner { top: 636px; }
  .abs { position: absolute; }

  /* ---------- outer spread ---------- */
  .masthead { left: 346px; top: 0; width: 346px; height: 99px; background: var(--black); text-align: center; }
  .brand-name { font-family: "Cinzel", serif; font-weight: 700; color: var(--gold); line-height: 1; }
  .masthead .brand-name--main { position: absolute; left: 0; right: 0; top: 26px; font-size: 31px; letter-spacing: 1px; }
  .masthead .brand-name--sub { position: absolute; left: 0; right: 0; top: 66px; font-size: 17px; letter-spacing: 6px; }

  .hero-photo { left: 220px; top: 99px; width: 472px; height: 310px;
    background: linear-gradient(100deg, #f1efea 0%, #e4e0d6 30%, #8c93a0 55%, #2c3b55 75%, #1b2a44 100%); }
  .hero-band { left: 253px; top: 338px; width: 439px; height: 71px; background: rgba(28,28,30,0.9); }
  .hero-headline { left: 253px; right: 0; top: 348px; text-align: center; color: var(--white);
    font-size: 14.5px; line-height: 16.8px; }
  .gold-band { left: 220px; top: 408px; width: 472px; height: 31px;
    background: linear-gradient(90deg, var(--gold-deep) 0%, var(--gold) 40%, var(--gold-light) 70%, var(--gold) 100%); }
  .gold-band-text { left: 253px; right: 0; top: 415px; text-align: center; color: var(--cream);
    font-family: "Playfair Display", serif; font-weight: 700; font-size: 15.5px; line-height: 17px; }
  .back-footer { left: 220px; top: 439px; width: 472px; height: 50px; background: var(--black); }
  .footer-brand { left: 234px; top: 451px; width: 90px; text-align: center; }
  .footer-brand .brand-name--main { font-size: 12.5px; display: block; }
  .footer-brand .brand-name--sub { font-size: 7px; letter-spacing: 3px; display: block; margin-top: 2px; }
  .footer-web { left: 346px; width: 346px; top: 459px; text-align: center; color: var(--white);
    font-size: 8.5px; letter-spacing: 3.6px; font-weight: 700; }

  .tram-photo { left: 33px; top: 179px; width: 220px; height: 207px;
    background: linear-gradient(160deg, #d6d6d6 0%, #9a9a9a 45%, #3c3c3c 100%); }

  .section-title { font-family: "Cinzel", serif; font-weight: 700; color: var(--gold-deep); font-size: 17px; line-height: 1; }
  .about-title { left: 34px; top: 34px; }
  .about-subtitle { left: 34px; top: 53px; font-family: "Tinos", serif; font-size: 11.2px; letter-spacing: 0.1px; }
  .rule { height: 1px; background: var(--gold-deep); }
  .about-rule { left: 34px; top: 72px; width: 268px; }
  .about-copy { left: 34px; top: 86px; width: 160px; font-size: 7.6px; line-height: 9.1px; text-align: justify; }

  .contact-list { left: 40px; top: 410px; list-style: none; font-size: 7.6px; line-height: 9px; }
  .contact-list li { display: flex; align-items: flex-start; margin-bottom: 7px; }
  .contact-list li:nth-child(3) { letter-spacing: 1.6px; }
  .contact-list svg { width: 6px; height: 6px; margin: 1px 6px 0 0; flex: none; }

  /* ---------- inner spread ---------- */
  .intro-copy { left: 34px; top: 35px; width: 279px; font-size: 7.6px; line-height: 9.1px; text-align: justify; }
  .church-photo { left: 34px; top: 96px; width: 402px; height: 263px;
    background: linear-gradient(170deg, #9a9a9a 0%, #5c5c5c 40%, #2a2a2a 80%, #3a3a3a 100%); }

  .how-title { left: 453px; top: 31px; font-family: "Cinzel", serif; font-weight: 400; font-size: 17.5px; color: var(--ink); }
  .how-rule { left: 453px; top: 55px; width: 209px; }
  .steps-line { left: 460px; top: 90px; width: 1px; height: 100px; border-left: 1px dotted #555; }
  .step-badge { width: 23px; height: 23px; border-radius: 50%;
    background: radial-gradient(circle at 40% 35%, var(--gold-light), var(--gold) 65%, var(--gold-deep));
    box-shadow: 0 0 0 1.5px #f2e6a8; font-family: "Tinos", serif; font-weight: 700; font-size: 10.5px;
    display: flex; align-items: center; justify-content: center; color: var(--ink); }
  .step-badge--1 { left: 449px; top: 70px; }
  .step-badge--2 { left: 449px; top: 122px; }
  .step-badge--3 { left: 449px; top: 179px; }
  .step-copy { left: 482px; width: 178px; font-size: 7.4px; line-height: 9.1px; text-align: justify; }
  .step-copy--1 { top: 73px; }
  .step-copy--2 { top: 110px; }
  .step-copy--3 { top: 176px; }

  .phone-photo { left: 408px; top: 222px; width: 252px; height: 237px;
    background: linear-gradient(135deg, #a9c6d3 0%, #7fa3b5 35%, #2f3f52 70%, #121a26 100%); }

  .cta-box { left: 34px; top: 378px; width: 355px; height: 81px; background: var(--charcoal); }
  .cta-line1 { left: 65px; top: 392px; font-family: "Cinzel", serif; font-size: 16px; color: var(--white); letter-spacing: 0.2px; }
  .cta-line2 { left: 65px; top: 411px; font-family: "Cinzel", serif; font-weight: 700; font-size: 15.5px; color: var(--gold-light); }
  .cta-pill { left: 63px; top: 436px; width: 240px; height: 33px; border-radius: 17px;
    background: linear-gradient(90deg, var(--gold-deep) 0%, var(--gold-light) 30%, var(--gold) 70%, var(--gold-light) 100%); }
  .cta-icon { left: 64px; top: 437px; width: 32px; height: 32px; border-radius: 50%; background: var(--ink);
    box-shadow: 0 0 0 2px var(--gold-light); display: flex; align-items: center; justify-content: center; }
  .cta-number { left: 107px; top: 436px; font-family: "Tinos", serif; font-weight: 700; font-size: 27px; line-height: 33px; color: var(--ink); }
  .bottom-rule { left: 0; top: 485px; width: 692px; height: 3px; background: linear-gradient(90deg, var(--gold-deep), var(--gold-light), var(--gold)); }
</style>
</head>
<body>

<section class="spread spread--outer" aria-label="Outer spread">
  <div class="abs hero-photo" role="img" aria-label="Businessman in a suit using a tablet, overlaid with a night city skyline and rising market chart lines"></div>
  <div class="abs tram-photo" role="img" aria-label="Black and white photo of a streetcar on a palm-lined city avenue"></div>

  <h2 class="abs section-title about-title">About</h2>
  <p class="abs about-subtitle">BRIGHTVALE CAPITAL AND GENERAL PARTNER</p>
  <div class="abs rule about-rule"></div>
  <p class="abs about-copy">Brightvale Capital was founded in 2019 by General Partner Marcus Whitfield Jr with a group economic empowerment mission. Marcus Whitfield has invested int stocks since a teenager received his BA in ecomics from Lakeshore State University and is currently attending Gulf Coast University,</p>

  <ul class="abs contact-list">
    <li><svg viewBox="0 0 10 10"><circle cx="5" cy="4" r="3" fill="none" stroke="#a88a22" stroke-width="1.4"/><path d="M5 7 L5 10" stroke="#a88a22" stroke-width="1.4"/></svg><span>Address line 1, Address line 1<br>Address line 2.</span></li>
    <li><svg viewBox="0 0 10 10"><circle cx="5" cy="5" r="4.2" fill="none" stroke="#a88a22" stroke-width="1.2"/><path d="M3.5 3 Q3.5 7 7 6.8" fill="none" stroke="#a88a22" stroke-width="1.2"/></svg><span>0123 456 789</span></li>
    <li><svg viewBox="0 0 10 10"><circle cx="5" cy="5" r="4.2" fill="none" stroke="#a88a22" stroke-width="1.2"/><path d="M1 5 H9 M5 1 V9" stroke="#a88a22" stroke-width="1"/></svg><span>www.BRIGHTVALECAPITAL.com</span></li>
  </ul>

  <header class="abs masthead">
    <span class="brand-name brand-name--main">BRIGHTVALE</span>
    <span class="brand-name brand-name--sub">CAPITAL</span>
  </header>

  <div class="abs hero-band"></div>
  <p class="abs hero-headline">Become a Partner and<br>Build Generational Wealth by Investing<br>In The Stock Market</p>
  <div class="abs gold-band"></div>
  <p class="abs gold-band-text">A First Of Its Kind Investment Club</p>
  <footer class="abs back-footer"></footer>
  <div class="abs footer-brand">
    <span class="brand-name brand-name--main">BRIGHTVALE</span>
    <span class="brand-name brand-name--sub">CAPITAL</span>
  </div>
  <p class="abs footer-web">www.BrightvaleCapital.com</p>
</section>

<section class="spread spread--inner" aria-label="Inner spread">
  <p class="abs intro-copy">If you are receiving this brochure its because someone sees you as a person that doesn’t want to just work and pay bills. Your someone who wants to build real generational wealth. Not throw schemes but the using the greatest wealth builder available. The stock market.</p>
  <div class="abs church-photo" role="img" aria-label="Black and white photo of a historic cathedral beside an iron fence and a narrow alley with balconies"></div>

  <h2 class="abs how-title">HOW IT WORKS</h2>
  <div class="abs rule how-rule"></div>
  <div class="abs steps-line"></div>
  <div class="abs step-badge step-badge--1">01</div>
  <div class="abs step-badge step-badge--2">02</div>
  <div class="abs step-badge step-badge--3">03</div>
  <p class="abs step-copy step-copy--1">Make initial deposit. The general partner will invest in stocks, bonds and other investment vehicles on your behalf.</p>
  <p class="abs step-copy step-copy--2">There is no upfront fees. The general p[partner will guarantee a 5 percent return and will work for free on your behalf until that is achieved. After the 5 percent return on the dollars invested the limited partner will receive 80 percent and the general partner will receive 20 percent of every dollar gained</p>
  <p class="abs step-copy step-copy--3">As the return and investments multiply the interests begins to compound annually. The legal partner legally owns shares of stock within the club and may redeem once a year or let money continue to earn interest.</p>

  <div class="abs phone-photo" role="img" aria-label="Hands holding a smartphone showing a trading chart, with market screens behind"></div>

  <div class="abs cta-box"></div>
  <p class="abs cta-line1">CALL US NOW</p>
  <p class="abs cta-line2">FOR A FREE CONSULTATION</p>
  <div class="abs cta-pill"></div>
  <div class="abs cta-icon">
    <svg width="16" height="16" viewBox="0 0 24 24" aria-hidden="true"><path d="M6.6 2.5 L9.5 2 L11 7 L8.8 8.6 C9.8 11 12.5 14 15.4 15.2 L17 13 L22 14.5 L21.5 17.4 C21 19.6 18.8 21.2 16.5 20.8 C9.5 19.4 4.6 14.5 3.2 7.5 C2.8 5.2 4.4 3 6.6 2.5 Z" fill="#ecd46a"/></svg>
  </div>
  <p class="abs cta-number">0123 456 789</p>
  <div class="abs bottom-rule"></div>
</section>

</body>
</html>
```